Business Card Re-Design/Update

We'd like to update out business cards. I've included our current "Style guide" which has the colour scheme of the organisation in it. I've also included the branding files with logos etc in them.

I've also included a copy of one of our existing cards so that you can see how ugly/dated they look. I'd like a fresh modern corporate look.

Target Market(s)

These are for our clients, potential clients, industry contacts - like all business cards

Contact Information for Business Card

Name
Position
Company Address - Level 1, 47 Garnet Lane, Toowong Qld 4066
Direct Phone
mobile
Email
Website -www.korvalnet.com.au
Logo

Colors

Designer to choose colors to be used in the design.

Requirements
Must have
• Main Logo
• Cards will need to be editable to be able to personalize them for each new employee.
Nice to have
• The MapOUT, HandOVER, UpKEEP would be okay to have if they can be sensibly and professionally added to the look without detracting from the main imagery.
• Maybe they could go on the back of the card? will leave this to your creative discretion as to whether/where they fit.
Should not have
• Should not have decorative or script fonts

```html
<!DOCTYPE html>
<html lang="en">
<head>
<meta charset="utf-8">
<title>korvalNET business card</title>
<link rel="stylesheet" href="https://fonts.googleapis.com/css2?family=Poppins:wght@500;600;700&family=Roboto+Condensed:wght@700&family=Open+Sans:wght@400;600&display=swap">
<style>
  :root {
    --backdrop: #3b3b3e;
    --card: #1f1f21;
    --card-edge: #2a2a2d;
    --white: #ffffff;
    --soft-white: #e9e9ea;
    --red: #e0262c;
    --green: #6aa83a;
    --blue: #1fa0dc;
    --magenta: #d62fbf;
    --divider: #8a8a8e;
  }
  * { box-sizing: border-box; margin: 0; padding: 0; }
  html, body { width: 1200px; height: 900px; overflow: hidden; }
  body {
    background: var(--backdrop);
    display: flex;
    flex-direction: column;
    align-items: center;
    justify-content: center;
    gap: 40px;
    font-family: "Open Sans", Arial, sans-serif;
  }
  .card {
    width: 680px;
    height: 388px;
    background: var(--card);
    border: 1px solid var(--card-edge);
    box-shadow: 0 10px 30px rgba(0,0,0,.45);
    position: relative;
  }

  /* Front */
  .card--front {
    display: flex;
    flex-direction: column;
    align-items: center;
    justify-content: center;
    gap: 56px;
  }
  .brand {
    display: flex;
    align-items: center;
    gap: 20px;
  }
  .brand__square {
    width: 54px; height: 54px;
    background: var(--red);
  }
  .brand__name {
    font-family: "Poppins", Arial, sans-serif;
    font-weight: 600;
    font-size: 56px;
    color: var(--white);
    letter-spacing: -0.5px;
    line-height: 1;
  }
  .services {
    display: flex;
    gap: 48px;
  }
  .service {
    display: flex;
    align-items: center;
    gap: 10px;
    font-family: "Poppins", Arial, sans-serif;
    font-weight: 600;
    font-size: 24px;
    line-height: 1;
  }
  .service__square { width: 22px; height: 22px; }
  .service--map { color: var(--green); }
  .service--map .service__square { background: var(--green); }
  .service--hand { color: var(--blue); }
  .service--hand .service__square { background: var(--blue); }
  .service--keep { color: var(--magenta); }
  .service--keep .service__square { background: var(--magenta); }

  /* Back */
  .card--back { padding: 0 56px; }
  .identity {
    position: absolute;
    left: 56px; top: 116px;
    width: 270px;
    text-align: right;
  }
  .identity__name {
    font-family: "Roboto Condensed", Arial Narrow, sans-serif;
    font-weight: 700;
    font-size: 30px;
    color: var(--red);
    text-transform: uppercase;
    letter-spacing: .3px;
  }
  .identity__role {
    font-size: 15px;
    color: var(--soft-white);
    margin-top: 2px;
  }
  .divider {
    position: absolute;
    left: 352px; top: 90px;
    width: 1px; height: 150px;
    background: linear-gradient(var(--card), var(--divider), var(--card));
  }
  .contacts {
    position: absolute;
    left: 376px; top: 92px;
    list-style: none;
  }
  .contacts li {
    display: flex;
    align-items: center;
    gap: 12px;
    font-size: 15.5px;
    color: var(--white);
    height: 24px;
  }
  .contacts svg, .address svg { width: 15px; height: 15px; fill: var(--red); flex: none; }
  .address {
    position: absolute;
    left: 0; right: 0; bottom: 52px;
    display: flex;
    justify-content: center;
    align-items: center;
    gap: 8px;
    font-size: 16.5px;
    color: var(--white);
  }
</style>
</head>
<body>

  <section class="card card--front">
    <div class="brand">
      <span class="brand__square"></span>
      <span class="brand__name">korvalNET</span>
    </div>
    <div class="services">
      <div class="service service--map"><span class="service__square"></span>MapOUT</div>
      <div class="service service--hand"><span class="service__square"></span>HandOVER</div>
      <div class="service service--keep"><span class="service__square"></span>UpKEEP</div>
    </div>
  </section>

  <section class="card card--back">
    <div class="identity">
      <h1 class="identity__name">Dana Whitfield</h1>
      <p class="identity__role">Business Development Manager</p>
    </div>
    <div class="divider"></div>
    <ul class="contacts">
      <li>
        <svg viewBox="0 0 24 24" aria-hidden="true"><path d="M6.6 10.8a15 15 0 0 0 6.6 6.6l2.2-2.2c.3-.3.7-.4 1-.2 1.1.4 2.3.6 3.6.6.6 0 1 .4 1 1V20c0 .6-.4 1-1 1A17 17 0 0 1 3 4c0-.6.4-1 1-1h3.5c.6 0 1 .4 1 1 0 1.3.2 2.5.6 3.6.1.3 0 .7-.2 1z"/></svg>
        +61 (0)7 3890 4410
      </li>
      <li>
        <svg viewBox="0 0 24 24" aria-hidden="true"><path d="M6.6 10.8a15 15 0 0 0 6.6 6.6l2.2-2.2c.3-.3.7-.4 1-.2 1.1.4 2.3.6 3.6.6.6 0 1 .4 1 1V20c0 .6-.4 1-1 1A17 17 0 0 1 3 4c0-.6.4-1 1-1h3.5c.6 0 1 .4 1 1 0 1.3.2 2.5.6 3.6.1.3 0 .7-.2 1z"/></svg>
        +61 (0)7 3890 4427
      </li>
      <li>
        <svg viewBox="0 0 24 24" aria-hidden="true"><path d="M7 1h10a2 2 0 0 1 2 2v18a2 2 0 0 1-2 2H7a2 2 0 0 1-2-2V3a2 2 0 0 1 2-2zm0 3v14h10V4zm5 15.5a1.2 1.2 0 1 0 0 2.4 1.2 1.2 0 0 0 0-2.4z"/></svg>
        +61 (0)412 605 318
      </li>
      <li>
        <svg viewBox="0 0 24 24" aria-hidden="true"><path d="M6 2h12v5H6zM3 8h18a2 2 0 0 1 2 2v7h-4v5H5v-5H1v-7a2 2 0 0 1 2-2zm4 8v4h10v-4z"/></svg>
        +61 (0)7 3890 4402
      </li>
      <li>
        <svg viewBox="0 0 24 24" aria-hidden="true"><path d="M2 5h20v14H2zm2 2v.5l8 5.5 8-5.5V7l-8 5.5z"/></svg>
        dwhitfield@korvalnet.com.au
      </li>
      <li>
        <svg viewBox="0 0 24 24" aria-hidden="true"><path d="M12 2a10 10 0 1 0 0 20 10 10 0 0 0 0-20zm-1 17.9A8 8 0 0 1 4.2 10L9 14.8v1a2 2 0 0 0 2 2zm6.9-2.5A2 2 0 0 0 16 16h-1v-3a1 1 0 0 0-1-1H8v-2h2a1 1 0 0 0 1-1V7h2a2 2 0 0 0 2-2v-.4a8 8 0 0 1 2.9 12.8z"/></svg>
        www.korvalnet.com.au
      </li>
    </ul>
    <p class="address">
      <svg viewBox="0 0 24 24" aria-hidden="true"><path d="M12 2a7 7 0 0 0-7 7c0 5.2 7 13 7 13s7-7.8 7-13a7 7 0 0 0-7-7zm0 9.5a2.5 2.5 0 1 1 0-5 2.5 2.5 0 0 1 0 5z"/></svg>
      Level 1, 47 Garnet Lane, Toowong Qld 4066
    </p>
  </section>

</body>
</html>
```